Plumbing Product Supply Company Needs Front & Back Cover Design For Instruction Manuals

We need a front and back over design for our instruction manuals that we need to give to clients.

There will also be a picture of the product on the front cover so please use the supplied image as dummy.

it needs to incorporate our logo and branding colours.

We are the industry leader so it needs to be up-market, professional and stand out from the crowd.

Target Market(s)

Plumbing Companies

Industry/Entity Type

Plumbing

Font styles to use
Sans Serif

Colors
abd036
ffffff
000000
eaeaea
cbcbcb

Requirements
Must have
• Front & Back Cover as it will become a booklet.
• The logo is to be on the black background.
Nice to have
• Professional, modern, sleek.
Should not have
• Other colours that what is on the guidelines.

```html
<!DOCTYPE html>
<html lang="en">
<head>
<meta charset="utf-8">
<title>Ridgeline Pipe Supply – Manual Cover Spread</title>
<link rel="stylesheet" href="https://fonts.googleapis.com/css2?family=Montserrat:wght@400;600&display=swap">
<style>
  :root {
    --green: #abd036;
    --white: #ffffff;
    --black: #000000;
    --light: #eaeaea;
    --mid: #cbcbcb;
    --board: #c4c4c2;
    --panel: #141414;
    --rule: #6e6e6e;
    --label: #5a5a5a;
  }
  html, body {
    margin: 0;
    padding: 0;
    overflow: hidden;
  }
  body {
    width: 855px;
    height: 1200px;
    background: var(--board);
    position: relative;
    font-family: "Montserrat", Arial, sans-serif;
  }
  .spread {
    position: absolute;
    left: 82px;
    top: 134px;
    width: 693px;
    height: 489px;
    display: block;
  }
  .side-label {
    position: absolute;
    top: 644px;
    margin: 0;
    font-size: 16px;
    font-weight: 400;
    color: var(--label);
    letter-spacing: 0.5px;
  }
  .side-label.back { left: 82px; }
  .side-label.front { left: 450px; }
  .brand-name { font-family: "Montserrat", Arial, sans-serif; font-weight: 600; fill: var(--green); }
  .body-copy { font-family: "Montserrat", Arial, sans-serif; font-size: 6.6px; fill: var(--mid); }
  .web-link { font-family: "Montserrat", Arial, sans-serif; font-size: 7px; font-weight: 600; fill: var(--green); }
</style>
</head>
<body>

<svg class="spread" viewBox="0 0 866 611" xmlns="http://www.w3.org/2000/svg" aria-label="Manual cover spread, back and front">
  <defs>
    <linearGradient id="brushed" x1="0" y1="0" x2="0" y2="1">
      <stop offset="0" stop-color="#8d8d8d"/>
      <stop offset="0.45" stop-color="#d6d6d6"/>
      <stop offset="1" stop-color="#9a9a9a"/>
    </linearGradient>
    <linearGradient id="brushed-v" x1="0" y1="0" x2="1" y2="0">
      <stop offset="0" stop-color="#8a8a8a"/>
      <stop offset="0.5" stop-color="#cfcfcf"/>
      <stop offset="1" stop-color="#8f8f8f"/>
    </linearGradient>
    <linearGradient id="product" x1="0" y1="0" x2="1" y2="1">
      <stop offset="0" stop-color="#f2f2f2"/>
      <stop offset="0.6" stop-color="#bdbdbd"/>
      <stop offset="1" stop-color="#3a3a3a"/>
    </linearGradient>
  </defs>

  <!-- dark perforated base -->
  <rect class="panel" x="0" y="0" width="866" height="611" fill="var(--panel)"/>

  <!-- brushed metal areas -->
  <path class="metal" d="M0 0 H206 V88 Q206 100 218 100 H290 Q302 100 302 112 V205 H0 Z" fill="url(#brushed)"/>
  <rect class="metal" x="745" y="0" width="121" height="280" fill="url(#brushed)"/>
  <rect class="metal" x="618" y="211" width="127" height="142" fill="url(#brushed-v)"/>
  <rect class="metal" x="553" y="353" width="140" height="258" fill="url(#brushed-v)"/>

  <!-- grey rules -->
  <g fill="none" stroke="var(--rule)" stroke-width="7">
    <line x1="0" y1="208" x2="302" y2="208"/>
    <line x1="306" y1="164" x2="618" y2="164"/>
    <path d="M618 0 V228 Q618 240 606 240 H590"/>
    <path d="M226 611 V385 Q226 373 238 373 H326 Q338 373 338 385 V446 Q338 458 350 458 H553"/>
    <line x1="693" y1="470" x2="693" y2="611"/>
  </g>

  <!-- green lines -->
  <g fill="none" stroke="var(--green)" stroke-width="7">
    <path d="M206 0 V88 Q206 100 218 100 H290 Q302 100 302 112 V353"/>
    <path d="M302 211 H728 Q743 211 743 226 V300"/>
    <line x1="743" y1="0" x2="743" y2="173"/>
    <line x1="553" y1="353" x2="553" y2="611"/>
  </g>

  <!-- spine fold -->
  <line x1="433" y1="0" x2="433" y2="611" stroke="var(--light)" stroke-width="1" stroke-dasharray="3 3"/>

  <!-- product photo placeholders -->
  <rect x="516" y="241" width="142" height="114" rx="18" fill="url(#product)" stroke="var(--rule)" stroke-width="7" role="img" aria-label="Product photo: pipelining supplies and kit case"/>
  <rect x="746" y="173" width="112" height="142" rx="18" fill="url(#product)" stroke="var(--green)" stroke-width="7" role="img" aria-label="Product photo: open tool case with lining supplies"/>
  <rect x="650" y="348" width="143" height="117" rx="18" fill="url(#product)" stroke="var(--green)" stroke-width="7" role="img" aria-label="Product photo: packers, rolls and fittings"/>

  <!-- back cover: brand and copy -->
  <text class="brand-name" x="33" y="450" font-size="13">Ridgeline</text>
  <text class="brand-name" x="33" y="464" font-size="7.5">PIPE SUPPLY</text>
  <text class="body-copy" x="26" y="502">Our supplies are built for the trade,</text>
  <text class="body-copy" x="26" y="510">tested on site and backed by people</text>
  <text class="body-copy" x="26" y="518">who know pipes. Every order ships fast</text>
  <text class="body-copy" x="26" y="526">from our own warehouse, with clear</text>
  <text class="body-copy" x="26" y="534">guides and real support when needed.</text>
  <text class="body-copy" x="26" y="542">Ask us about bulk pricing and kits.</text>
  <text class="web-link" x="26" y="581">WWW.RIDGELINEPIPE.COM</text>

  <!-- front cover: brand on black -->
  <rect x="714" y="519" width="118" height="60" fill="var(--black)"/>
  <text class="brand-name" x="722" y="549" font-size="19">Ridgeline</text>
  <text class="brand-name" x="722" y="568" font-size="10">PIPE SUPPLY</text>
</svg>

<p class="side-label back">BACK</p>
<p class="side-label front">FRONT</p>

</body>
</html>
```